Website Landing Page for Brightfall Systems

Create a custom designed website landing page for our business. Looking for a professional upscale design that incorporates our logo and logo colors into the theme. I want a standard fixed frame website, not a constant scrolling format that seems to be the trend. To start with I'm looking for more of the graphic design part, maybe a concept or theme, I don't expect to see a finished project. Not interested in generic templates or layouts.

The name of our company is Brightfall Systems and I've attached our logo below. I'd like to have the web page have the same look and feel of our logo, as well as the colors. Our company, Brightfall Systems does system design, installation, and programming, of residential and commercial Audio/Video and Automation systems. We do home theaters, lighting and building automation, video conferencing systems, security camera installations, conference rooms, projectors, distributed audio systems, and similar Technology projects. This will be a professional services/informational website. We will not sell products on this website. This website will be used to advertise our company and communicate our services to prospective customers. Having a well designed, professional and clean website is one way we want to distinguish our company from the competition.

Here are some examples of what I consider a professional well designed website
http://www.qorlamstudio.com/Work/

Last year we had our tradlo store designed (with PixelMarket) and I'm really happy with the way it turned out. You can see it at www.HolvenGearDepot.com I consider this to be a great design and looking for the same level of quality with this new website. However, do not copy or use any part of this design in this new project. This tradlo store is completely separate from our other company Brightfall Systems. I only mention this tradlo store an an example of good work.

Reason: Still going through designs.

Reason: Still working on project and have not had time to review all designs and request revisions.

Reason: Sill going through designs and requesting revisions

Reason: still going through all the submissions we received.

Target Market(s)

People interested in Audio/Video, home theaters, home automation. We do sales, system design, and programming. We typically work on larger projects with both residential and commercial customers.

Industry/Entity Type

Business

Number of Pages Required

1 page

Requirements
Must have
• Great design elements. Please use a white background. I think white goes well with our logo colors.

```html
<!DOCTYPE html>
<html lang="en">
<head>
<meta charset="utf-8">
<title>Brightfall Systems</title>
<link href="https://fonts.googleapis.com/css2?family=Open+Sans:wght@400;700&display=swap" rel="stylesheet">
<style>
  :root {
    --green: #9ecf3a;
    --blue: #3f7fc0;
    --button: #4a88c8;
    --ink: #1e1e1e;
    --white: #ffffff;
    --sky-top: #2f63b6;
    --sky-mid: #6f9bd2;
    --glass: #8fb0cf;
    --facade: #c9d3dc;
  }
  * { margin: 0; padding: 0; box-sizing: border-box; }
  html, body { width: 1200px; height: 639px; overflow: hidden; background: var(--white); }
  body { font-family: "Open Sans", sans-serif; color: var(--ink); }
  .page { position: relative; width: 1200px; height: 639px; overflow: hidden; background: var(--white); }

  .hero-photo {
    position: absolute; left: 0; top: 0; width: 1200px; height: 566px;
    background:
      linear-gradient(180deg, rgba(47,99,182,0) 0%, rgba(47,99,182,0) 30%, rgba(160,185,210,0.35) 100%),
      linear-gradient(100deg, var(--facade) 0%, var(--glass) 20%, var(--sky-mid) 45%, var(--glass) 65%, var(--facade) 90%, var(--sky-top) 100%),
      var(--sky-top);
  }
  .hero-photo::before {
    content: ""; position: absolute; inset: 0;
    background: linear-gradient(180deg, var(--sky-top) 0%, rgba(47,99,182,0.25) 40%, rgba(47,99,182,0) 60%);
  }

  .service-tile {
    position: absolute; width: 198px; height: 171px;
    background: var(--green); color: var(--white);
    display: flex; align-items: center; justify-content: center; text-align: center;
    font-weight: 700; font-size: 21px; line-height: 28px;
  }
  .tile-security { left: 206px; top: 0; height: 169px; }
  .tile-video { left: 779px; top: 0; height: 170px; }
  .tile-audio { left: 0; top: 181px; width: 197px; height: 172px; }
  .tile-lighting { left: 977px; top: 205px; width: 197px; height: 172px; }
  .tile-design { left: 231px; top: 360px; height: 172px; }
  .tile-theater { left: 735px; top: 395px; height: 171px; }

  .intro-circle {
    position: absolute; left: 434px; top: 100px; width: 318px; height: 318px;
    border-radius: 50%; background: rgba(255,255,255,0.88);
    text-align: center;
  }
  .intro-title {
    margin-top: 78px; color: var(--blue); font-weight: 700; font-size: 32px; line-height: 40px;
  }
  .intro-text {
    margin: 6px auto 0; width: 272px; font-size: 10px; line-height: 12.6px; color: var(--ink);
  }
  .intro-button {
    display: inline-block; margin-top: 11px; width: 105px; height: 27px; line-height: 27px;
    border-radius: 14px; background: var(--button); color: var(--white); font-size: 11.5px;
    text-decoration: none;
  }

  .footer-tab { position: absolute; left: 0; top: 532px; width: 445px; height: 40px; background: var(--white); }
  .site-footer { position: absolute; left: 0; top: 566px; width: 1200px; height: 73px; background: var(--white); }

  .brand { position: absolute; left: 209px; top: 554px; display: flex; align-items: center; gap: 12px; }
  .brand-mark { width: 64px; height: 64px; border-radius: 50%; border: 6px solid var(--blue); }
  .brand-name {
    font-size: 17px; line-height: 19px; font-weight: 400; color: var(--blue);
    letter-spacing: 0.5px; width: 120px;
  }

  .main-nav { position: absolute; top: 582px; left: 448px; display: flex; gap: 22px; }
  .main-nav a {
    display: block; width: 60px; text-align: center; color: var(--ink); text-decoration: none;
    font-size: 13px; line-height: 16px; padding-bottom: 7px; border-bottom: 3px solid var(--button);
  }
  .main-nav a:first-child { width: 62px; }

  .social { position: absolute; left: 687px; top: 598px; display: flex; gap: 10px; }
  .social span { display: block; width: 13px; height: 13px; border-radius: 50%; background: var(--button); }

  .info-nav { position: absolute; left: 826px; top: 596px; display: flex; align-items: center; font-size: 10.5px; letter-spacing: 1.6px; }
  .info-nav a { color: var(--ink); text-decoration: none; padding: 0 7px; line-height: 16px; }
  .info-nav a:first-child { padding-left: 0; border-right: 1px solid var(--button); }
</style>
</head>
<body>
<div class="page">
  <div class="hero-photo" role="img" aria-label="Photograph of a modern glass office building under a blue sky with white clouds"></div>

  <div class="service-tile tile-security">Security<br>Camera<br>Installations</div>
  <div class="service-tile tile-video">Video<br>Conferencing<br>Systems</div>
  <div class="service-tile tile-audio">Distributed<br>Audio<br>Systems</div>
  <div class="service-tile tile-lighting">Lighting<br>Building<br>Automation</div>
  <div class="service-tile tile-design">System design<br>Installation<br>Programming</div>
  <div class="service-tile tile-theater">Home<br>Theaters<br>Projectors</div>

  <section class="intro-circle">
    <h1 class="intro-title">Who we are?</h1>
    <p class="intro-text">Brightfall Systems does system design, installation, and programming, of residential and commercial Audio/Video and Automation systems.<br>We do home theaters, lighting and building automation, video conferencing systems, security camera installations, conference rooms, projectors, distributed audio systems, and similar Technology projects.</p>
    <a class="intro-button" href="#">Find out more</a>
  </section>

  <div class="footer-tab"></div>
  <footer class="site-footer"></footer>

  <div class="brand">
    <span class="brand-mark"></span>
    <span class="brand-name">BRIGHTFALL SYSTEMS</span>
  </div>

  <nav class="main-nav">
    <a href="#">Our<br>Products</a>
    <a href="#">Our<br>Services</a>
  </nav>

  <div class="social" aria-label="Social links">
    <span></span><span></span>
  </div>

  <nav class="info-nav">
    <a href="#">About Us</a>
    <a href="#">Contact Us</a>
  </nav>
</div>
</body>
</html>
```